Digitalization Training Site - Koru Theme (mandatory)

Hi,
I have a Koru theme website running on Wordpress and I need a design.

Designs must be possible with standard Koru theme and minimal/no CSS customization or similar. if this is required please note this in submission. Also, please note mobile and device usage which must be universal.

Koru Theme:
https://www.brightlanestudio.example

Target Market: education, online training, IT training, digitalization, digital transformation, disruption

Target Group: IT students, IT Management students, IT companies showing examples, IT companies recruiting, lectures, trainers, training companies

Look and Feel:
- Elegant, Playful, Fresh, Plain, Personable, Economical

Main Colors:
- Background: mainly white/light grey (like logo), a few parts maybe in orange (like the logo colors)
- design elements: logo colors (grey, dark yellow – orange, and one extra color: a darker blue that fits to the logo colors)
- text: grey, black, white - depending on background, good readable

Form
- round buttons
- full with
- responsive for desktop, tablet and mobile (koru is supporting this ;)
- animation like on the Koru layout for e-courses (see below)

I have attached:
- logo files (ai, png, jpg, eps)
- some design parts that I like (samples for blocks)

To be delivered:
- koru layout (zipped json files)
- all pictures, icons, and illustrations (high res. : ai, psd, eps, jpg, png)

There is a Koru Layout for e-courses that is partly interesting you can find it here:
- https://www.brightlanestudio.example/blog/koru-resources/download-a-free-breathtaking-learning-management-lms-layout-pack-for-koru
- Can be used as idea for building blocks

I need at least 20 building blocks (see examples I uploaded) for homepage, landing page, shop, product page, marketing, landing, about us, etc. The building blocks could be
- Slider (for home page) (I like the light bulbs in one of the examples)
- Content blocks with illustrations
- Get started area (free & premium)
- Choose a plan
- Our Process (5-6 steps)
- Woocommerce shop page
- Woocommerce product page
- We offer
- Footer
I like the footer animation in this example: http://demo.korumodules.example/koru-edu//gallery/
- Contact
- see Koru Layout example for more Blocks
NOT:
- Newsletter

Best regards
Marten

Target Market(s)

Industry/Entity Type

Training

Coding

Coded - Design and coding required

Number of Pages Required

5+ page

Font styles to use
Serif

Colors
ffcf3e
ffc214
faa54b
f78f20
f68e4e
f37122
3276b5
99b9da
959595

Requirements
Must have
• Designs must be possible with standard Koru theme and minimal/no CSS customization or similar. if this is required please note this in submission. Also, please note mobile and device usage which must be universal.
• adopt design preference (logo colors etc. - see big text)
• To be delivered:
• - koru layout (zipped json files)
• - all pictures, icons, and illustrations (high res. : ai, psd, eps, jpg, png)
Nice to have
• Ideas for good design for a online-course site

```html
<!DOCTYPE html>
<html lang="en">
<head>
<meta charset="utf-8">
<title>Northfield Learning Hub – Home</title>
<link rel="stylesheet" href="https://fonts.googleapis.com/css2?family=Open+Sans:wght@400;600;700&display=swap">
<style>
  :root {
    --white: #ffffff;
    --hero-grey: #808080;
    --nav-text: #666666;
    --nav-active: #2ea3f2;
    --brand-orange: #f37122;
    --brand-grey: #6f6f6f;
    --button-text: #f05a1e;
    --visual-top: #7a7a7a;
    --visual-bottom: #858079;
  }
  * { box-sizing: border-box; margin: 0; padding: 0; }
  html, body {
    width: 1200px; height: 411px; overflow: hidden;
    font-family: "Open Sans", Arial, sans-serif;
    background: var(--white);
  }
  .site { position: relative; width: 1200px; height: 411px; overflow: hidden; }

  .site-header {
    position: absolute; top: 0; left: 0; width: 1200px; height: 81px;
    background: var(--white);
    box-shadow: 0 1px 4px rgba(0,0,0,0.18);
    z-index: 2;
  }
  .brand {
    position: absolute; left: 113px; top: 24px;
    display: flex; align-items: center; gap: 10px;
  }
  .brand-mark { width: 30px; height: 30px; background: var(--brand-orange); }
  .brand-name { font-size: 20px; font-weight: 600; color: var(--brand-grey); line-height: 1; }

  .main-nav { position: absolute; top: 30px; left: 0; width: 1200px; height: 22px; }
  .main-nav a {
    position: absolute; top: 0;
    font-size: 15.5px; font-weight: 600; color: var(--nav-text);
    text-decoration: none; letter-spacing: 0.6px; line-height: 22px;
  }
  .main-nav a.is-active { color: var(--nav-active); }
  .search-icon { position: absolute; left: 1062px; top: 33px; }

  .hero {
    position: absolute; top: 81px; left: 0; width: 1200px; height: 330px;
    background: var(--hero-grey);
  }
  .hero-bands { position: absolute; inset: 0; }
  .hero-title {
    position: absolute; left: 126px; top: 56px;
    font-size: 34px; font-weight: 700; color: var(--white);
    text-shadow: 0 1px 3px rgba(0,0,0,0.35); line-height: 46px;
    white-space: nowrap;
  }
  .hero-text {
    position: absolute; left: 126px; top: 110px; width: 440px;
    font-size: 16px; line-height: 31px; color: var(--white);
    white-space: nowrap;
  }
  .hero-button {
    position: absolute; left: 126px; top: 219px; width: 159px; height: 59px;
    border-radius: 30px; background: var(--white);
    color: var(--button-text); font-size: 18px; font-weight: 700; letter-spacing: 0.8px;
    display: flex; align-items: center; justify-content: center; text-decoration: none;
  }
  .hero-visual {
    position: absolute; left: 786px; top: 4px; width: 214px; height: 244px;
    background: linear-gradient(180deg, var(--visual-top), var(--visual-bottom));
  }
  .slider-dots {
    position: absolute; left: 573px; top: 298px; display: flex; gap: 7px;
  }
  .slider-dots span { width: 7px; height: 7px; border-radius: 50%; background: rgba(255,255,255,0.5); }
  .slider-dots span.is-current { background: var(--white); }
</style>
</head>
<body>
<div class="site">
  <header class="site-header">
    <div class="brand">
      <span class="brand-mark"></span>
      <span class="brand-name">Northfield Learning Hub</span>
    </div>
    <nav class="main-nav">
      <a class="is-active" href="#" style="left:683px">Home</a>
      <a href="#" style="left:750px">About Us</a>
      <a href="#" style="left:844px">Shop</a>
      <a href="#" style="left:906px">Marketing</a>
      <a href="#" style="left:1009px">Blog</a>
    </nav>
    <svg class="search-icon" width="16" height="17" viewBox="0 0 16 17" aria-label="Search">
      <circle cx="9.5" cy="6.5" r="5" fill="none" stroke="#666" stroke-width="1.6"/>
      <line x1="6" y1="10.2" x2="1.5" y2="15" stroke="#666" stroke-width="1.8" stroke-linecap="round"/>
    </svg>
  </header>

  <section class="hero">
    <svg class="hero-bands" width="1200" height="330" viewBox="0 0 1200 330" aria-hidden="true">
      <polygon points="0,40 330,0 420,0 0,120" fill="#858585"/>
      <polygon points="700,330 1200,150 1200,230 950,330" fill="#868686"/>
      <polygon points="950,330 1200,230 1200,330" fill="#8b8b8b"/>
    </svg>
    <div class="hero-visual" role="img" aria-label="Illustration of hanging light bulbs, one glowing orange"></div>
    <h1 class="hero-title">Northfield Learning Hub</h1>
    <p class="hero-text">Class aptent taciti sociosqu ad litora torquent per<br>conubia nostra, per inceptos himenaeos. Sed molestie,<br>velit ut eleifend sollicitudin, neque orci tempor nulla.</p>
    <a class="hero-button" href="#">Read More</a>
    <div class="slider-dots"><span class="is-current"></span><span></span><span></span></div>
  </section>
</div>
</body>
</html>
```